Talbrin Business Cards

Front and back. Simon Kavelle MBA is the CEO of Talbrin Homes. Black white and grays. Logo and cool design.

Target Market(s)

Professional lenders and investors

Industry/Entity Type

Real estate developer. NO HOUSES OR ROOFS

Contact Information for Business Card

Logo, name and unique design. Front and back. Simon Kavelle MBA is the CEO of Talbrin Homes. Black white and grays. Logo and cool design.

Font styles to use
Sans Serif

Colors

Designer to choose only greyscale colors for use in the design.

Requirements
Must have
• Cool look. Not the same card I could design.
Nice to have
• Something memorable
Should not have
• Basic

```html
<!DOCTYPE html>
<html lang="en">
<head>
<meta charset="utf-8">
<title>Talbrin Homes – Business Cards</title>
<link rel="stylesheet" href="https://fonts.googleapis.com/css2?family=Roboto:wght@400;500;700;900&display=swap">
<style>
  :root {
    --backdrop: #a8a8a8;
    --ink: #0a0a0a;
    --paper: #ffffff;
    --paper-shade: #ececec;
    --text-muted: #6f6f6f;
    --text-body: #4a4a4a;
    --rule: #8a8a8a;
  }
  * { box-sizing: border-box; margin: 0; padding: 0; }
  html, body {
    width: 1200px;
    height: 1056px;
    overflow: hidden;
    background: var(--backdrop);
    font-family: "Roboto", Arial, sans-serif;
  }
  .sheet {
    width: 1200px;
    height: 1056px;
    display: flex;
    flex-direction: column;
    align-items: center;
    justify-content: center;
    gap: 64px;
  }
  .card {
    width: 700px;
    height: 400px;
    position: relative;
    box-shadow: 0 14px 30px rgba(0,0,0,0.22);
  }
  .card--front {
    background: var(--ink);
    display: flex;
    align-items: center;
    justify-content: center;
  }
  .wordmark {
    font-family: "Roboto", Arial, sans-serif;
    font-weight: 900;
    letter-spacing: -1px;
    line-height: 1;
    white-space: nowrap;
  }
  .card--front .wordmark {
    color: var(--paper);
    font-size: 64px;
  }
  .card--back {
    background: var(--paper);
    display: grid;
    grid-template-columns: 45% 55%;
  }
  .brand-panel {
    display: flex;
    align-items: center;
    justify-content: center;
    background: linear-gradient(90deg, var(--paper) 80%, var(--paper-shade) 100%);
  }
  .card--back .wordmark {
    color: var(--ink);
    font-size: 40px;
  }
  .contact-panel {
    padding: 92px 0 0 40px;
  }
  .contact-name {
    font-size: 24px;
    font-weight: 700;
    color: var(--ink);
  }
  .contact-role {
    font-size: 16px;
    color: var(--text-muted);
    margin-top: 4px;
  }
  .contact-rule {
    width: 96px;
    height: 1px;
    background: var(--rule);
    margin: 14px 0 16px;
  }
  .contact-list { list-style: none; }
  .contact-item {
    display: flex;
    align-items: center;
    gap: 10px;
    font-size: 17px;
    color: var(--text-body);
    margin-bottom: 12px;
  }
  .contact-icon {
    width: 24px;
    height: 24px;
    flex: none;
  }
</style>
</head>
<body>
<main class="sheet">
  <section class="card card--front" aria-label="Card front">
    <span class="wordmark">Talbrin Homes</span>
  </section>

  <section class="card card--back" aria-label="Card back">
    <div class="brand-panel">
      <span class="wordmark">Talbrin Homes</span>
    </div>
    <div class="contact-panel">
      <h1 class="contact-name">Simon Kavelle MBA</h1>
      <p class="contact-role">CEO of Talbrin Homes</p>
      <div class="contact-rule"></div>
      <ul class="contact-list">
        <li class="contact-item">
          <svg class="contact-icon" viewBox="0 0 24 24" aria-hidden="true">
            <rect width="24" height="24" rx="4" fill="#0a0a0a"/>
            <path d="M8 5.5l2 .3 1 3-1.4 1.2a8 8 0 0 0 4.4 4.4l1.2-1.4 3 1 .3 2c-.2 1-1 1.5-2 1.5A11 11 0 0 1 6.5 7.5c0-1 .5-1.8 1.5-2z" fill="#fff"/>
          </svg>
          (000) 123-4567
        </li>
        <li class="contact-item">
          <svg class="contact-icon" viewBox="0 0 24 24" aria-hidden="true">
            <rect width="24" height="24" rx="4" fill="#0a0a0a"/>
            <rect x="5" y="7" width="14" height="10" fill="none" stroke="#fff" stroke-width="1.5"/>
            <path d="M5 7l7 6 7-6" fill="none" stroke="#fff" stroke-width="1.5"/>
          </svg>
          info@talbrinhomes.com
        </li>
        <li class="contact-item">
          <svg class="contact-icon" viewBox="0 0 24 24" aria-hidden="true">
            <rect width="24" height="24" rx="4" fill="#0a0a0a"/>
            <path d="M7 5l10 7-4.3.8 2.6 4.6-1.6.9-2.6-4.6L8 17z" fill="#fff"/>
          </svg>
          www.talbrinhomes.com
        </li>
      </ul>
    </div>
  </section>
</main>
</body>
</html>
```